***Dappled Fern Lash Studio is in need of a web site makeover***

I need a makeover for my existing web site. www.dappled-fern.com

Please help!!!! Thanks 😁

Dappled Fern Lash Studio is an eyelash extension salon. In addition, we also provide skincare services (facials, waxing, etc). Our web site needs to appear professional and intuitive. In addition, allowing for ease of online booking is of utmost importance.

The client web site experience:
- esthetically pleasing and makes sense
- clearly recognize brand (Dappled Fern)
- easy to follow web pages
- easy to book appointments online
- easy to sign up for email updates
- easily locate services menu and pricing

Target Market(s)

Dappled Fern Lash Studio offers eyelash extension services, as well as various skincare services (I.e. facials, waxing, etc.)

Industry/Entity Type

Beauty Salon

Number of Pages Required

5+ page

Font styles to use
Sans Serif
Script

Colors
000000
fee3d5
eaeaea
ffffff

Requirements
Must have
• - Home page with static contact information
• - Services page (menu of services and pricing)
• - Photo gallery page
• - Contact page
• - Q&A page
Nice to have
• Professional, classy, intuitive and simple for clients to be able to book online.

```html
<!DOCTYPE html>
<html lang="en">
<head>
<meta charset="utf-8">
<title>Dappled Fern Lash Studio</title>
<link rel="stylesheet" href="https://fonts.googleapis.com/css2?family=Great+Vibes&family=Open+Sans:wght@400;600;700&display=swap">
<style>
:root{
  --magenta:#e4197c;
  --magenta-dark:#b80f60;
  --pink-soft:#fbe1ee;
  --pink-mid:#f5bfd8;
  --pink-band:#f2a9cb;
  --ink:#333333;
  --panel:#2b2a2c;
  --white:#ffffff;
  --grey:#eaeaea;
  --script:"Great Vibes",cursive;
  --sans:"Open Sans",Arial,sans-serif;
}
*{box-sizing:border-box;margin:0;padding:0}
html,body{width:1200px;height:2496px;overflow:hidden}
body{font-family:var(--sans);color:var(--ink);background:var(--pink-soft)}
.canvas{width:1200px;height:2496px;position:relative;overflow:hidden}
.script-title{font-family:var(--script);color:var(--magenta);font-size:46px;text-align:center;font-weight:400}
.body-copy{font-size:15px;line-height:24px;text-align:center;color:#555}
.btn-outline{display:inline-block;border:2px solid var(--magenta);border-radius:6px;padding:8px 26px;font-size:13px;font-weight:600;letter-spacing:1px;text-transform:uppercase;color:var(--ink);background:var(--white)}

/* header */
.site-header{height:140px;background:linear-gradient(#fff,#fde9f2);position:relative}
.brand{position:absolute;left:50%;top:14px;transform:translateX(-50%);text-align:center;color:var(--magenta);font-weight:700;line-height:1.05;background:#fff;padding:8px 34px;border-radius:0 0 12px 12px}
.brand .brand-name{font-size:30px}
.brand .brand-sub{font-size:22px}
.brand .brand-tag{font-size:12px;letter-spacing:2px;margin-top:4px}
.header-tools{position:absolute;right:40px;top:22px;display:flex;align-items:center;gap:8px}
.social-dot{width:26px;height:26px;border-radius:50%;background:var(--magenta)}
.book-link{font-family:var(--script);color:var(--magenta);font-size:26px;margin-left:18px}
.main-nav{position:absolute;top:100px;left:60px;right:60px;display:flex;justify-content:space-between;font-family:var(--script);font-size:25px;color:var(--magenta)}
.main-nav .gap{width:230px}
.main-nav .active{border-bottom:3px solid var(--magenta)}

/* hero */
.hero{height:520px;position:relative;padding:6px 60px 0}
.hero-frame{height:450px;border:4px solid var(--magenta);border-radius:26px;overflow:hidden;position:relative}
.hero-image{position:absolute;inset:0;background:linear-gradient(100deg,#e7a6c9 0%,#cf79b0 35%,#8a4a9c 62%,#4a1f6e 82%,#2c0f44 100%)}
.hero-arrow{position:absolute;top:50%;transform:translateY(-50%);width:40px;height:60px}
.hero-arrow.prev{left:14px}.hero-arrow.next{right:14px}
.hero-dots{display:flex;justify-content:center;gap:10px;margin-top:22px}
.hero-dots span{width:10px;height:10px;border-radius:50%;background:#d8a0bd}
.hero-dots span.on{background:var(--magenta)}

/* about */
.about{height:300px;padding:36px 150px 0;text-align:center;background:var(--pink-mid)}
.about .body-copy{margin:14px 0 22px}

/* services */
.services{height:370px;display:flex}
.service-card{flex:1;position:relative;text-align:center;padding:40px 46px 0;color:var(--white)}
.service-card.lash{background:linear-gradient(90deg,#1d1c1e,#3a3438 70%,#5a4d52)}
.service-card.skin{background:linear-gradient(90deg,#5b4f53,#8a7a7c 50%,#b9a39f)}
.service-card .body-copy{color:#eee;margin:14px 0 28px}
.service-card .btn-outline{background:transparent;color:#fff;border-color:#fff}

/* gallery */
.gallery{height:380px;background:var(--pink-band);padding:30px 0 0;text-align:center;position:relative}
.thumbs{display:flex;justify-content:center;gap:20px;margin:22px 0 24px}
.thumb{width:176px;border:4px solid #fff;background:#fff}
.thumb-image{height:140px;background:linear-gradient(135deg,#f3d2c5,#c98f86 60%,#6e4a4a)}
.thumb-caption{background:var(--magenta);color:#fff;font-size:11px;text-align:left;padding:4px 6px;line-height:14px}
.gallery-arrow{position:absolute;top:180px;width:20px;height:34px}
.gallery-arrow.prev{left:60px}.gallery-arrow.next{right:60px}

/* faq */
.faq{height:250px;padding:36px 150px 0;text-align:center;background:var(--pink-soft)}
.faq .body-copy{margin:14px 0 22px}

/* booking */
.booking{height:390px;padding:26px 90px 0;background:var(--pink-mid)}
.booking-card{margin-top:14px;background:#fff;border:3px solid var(--magenta);border-radius:10px;overflow:hidden}
.tabs{display:flex;background:var(--pink-soft);border-bottom:3px solid var(--magenta)}
.tab{padding:12px 36px;font-size:14px;font-weight:600;color:var(--magenta)}
.tab.active{background:var(--magenta);color:#fff}
.booking-form{display:grid;grid-template-columns:1fr 1fr 1fr;gap:16px 26px;padding:26px 26px 22px}
.field{height:36px;border:1px solid #ccc;border-radius:4px;font-size:13px;color:#777;padding:9px 12px;display:flex;justify-content:space-between;align-items:center}
.field.message{grid-row:span 2;height:88px;align-items:flex-start}
.actions{display:flex;gap:14px}
.actions .submit,.actions .reset{flex:1;height:36px;border-radius:4px;font-size:13px;font-weight:700;display:flex;align-items:center;justify-content:center;letter-spacing:1px}
.submit{background:var(--magenta);color:#fff}
.reset{background:#bdbdbd;color:#fff}

/* footer */
.site-footer{height:146px;background:linear-gradient(#f6b9d4,#ec86b3);position:relative;display:flex;padding:22px 60px 0;gap:50px}
.site-footer::after{content:"";position:absolute;left:0;right:0;bottom:0;height:14px;background:var(--magenta-dark)}
.footer-brand{color:var(--magenta-dark);font-weight:700;font-size:22px;line-height:1.1;width:240px}
.footer-brand small{display:block;font-size:11px;letter-spacing:2px;margin-top:4px}
.footer-col{font-size:12px;line-height:18px;color:#3a2230}
.footer-col h4{font-size:13px;margin-bottom:4px}
.footer-right{margin-left:auto;text-align:right;font-size:11px;color:#3a2230}
.footer-right .social{display:flex;gap:8px;justify-content:flex-end;margin-bottom:16px}
</style>
</head>
<body>
<div class="canvas">

<header class="site-header">
  <div class="brand">
    <div class="brand-name">Dappled Fern</div>
    <div class="brand-sub">lash studio</div>
    <div class="brand-tag">beauty + wellness</div>
  </div>
  <div class="header-tools">
    <span class="social-dot"></span><span class="social-dot"></span><span class="social-dot"></span><span class="social-dot"></span>
    <span class="book-link">Book Appointment</span>
  </div>
  <nav class="main-nav">
    <span class="active">Home</span><span>About Us</span><span>Eyelash Extension Services</span>
    <span class="gap"></span>
    <span>Skincare Services</span><span>Photo Gallery</span><span>FAQs</span><span>Contact Us</span>
  </nav>
</header>

<section class="hero">
  <div class="hero-frame">
    <div class="hero-image" role="img" aria-label="Close-up photo of an eye with long lash extensions and pink eyeshadow beside a purple iris flower"></div>
    <svg class="hero-arrow prev" viewBox="0 0 40 60"><path d="M28 8 L10 30 L28 52" fill="none" stroke="#fff" stroke-width="4"/></svg>
    <svg class="hero-arrow next" viewBox="0 0 40 60"><path d="M12 8 L30 30 L12 52" fill="none" stroke="#fff" stroke-width="4"/></svg>
  </div>
  <div class="hero-dots"><span class="on"></span><span></span><span></span><span></span></div>
</section>

<section class="about">
  <h2 class="script-title">About Dappled Fern Lash Studio</h2>
  <p class="body-copy">Our studio is a calm, welcoming space devoted to beautiful lashes and healthy skin. Each certified lash artist tailors every set to your eye shape and lifestyle, using gentle adhesives and premium lashes for comfort that lasts. Beyond lashes, we offer facials, waxing and skin treatments designed to refresh and restore. Book online in minutes, join our email list for seasonal offers, and let us help you wake up feeling polished, confident and ready for your day.</p>
  <span class="btn-outline">Read More</span>
</section>

<section class="services">
  <div class="service-card lash" role="img" aria-label="Background photo of a woman with lash extensions">
    <h2 class="script-title">Eyelash Extension Services</h2>
    <p class="body-copy">Classic, hybrid and volume sets applied lash by lash for a natural or dramatic look. Refills, lash lifts and tinting keep your lashes full and fresh between visits. View the full menu and pricing.</p>
    <span class="btn-outline">Discover More</span>
  </div>
  <div class="service-card skin" role="img" aria-label="Background photo of a woman enjoying a facial treatment">
    <h2 class="script-title">Skincare Services</h2>
    <p class="body-copy">Custom facials, peels, brow shaping and gentle waxing for every skin type. Our estheticians listen first, then build a treatment that leaves skin clear, soft and glowing. See services and pricing.</p>
    <span class="btn-outline">Discover More</span>
  </div>
</section>

<section class="gallery">
  <h2 class="script-title">Photo Gallery</h2>
  <svg class="gallery-arrow prev" viewBox="0 0 20 34"><path d="M16 3 L4 17 L16 31" fill="none" stroke="#fff" stroke-width="3"/></svg>
  <svg class="gallery-arrow next" viewBox="0 0 20 34"><path d="M4 3 L16 17 L4 31" fill="none" stroke="#fff" stroke-width="3"/></svg>
  <div class="thumbs">
    <figure class="thumb"><div class="thumb-image" role="img" aria-label="Lash extension result photo"></div><figcaption class="thumb-caption">Image 1<br>Classic full set</figcaption></figure>
    <figure class="thumb"><div class="thumb-image" role="img" aria-label="Lash extension result photo"></div><figcaption class="thumb-caption">Image 2<br>Hybrid volume set</figcaption></figure>
    <figure class="thumb"><div class="thumb-image" role="img" aria-label="Lash extension result photo"></div><figcaption class="thumb-caption">Image 3<br>Soft natural look</figcaption></figure>
    <figure class="thumb"><div class="thumb-image" role="img" aria-label="Lash extension result photo"></div><figcaption class="thumb-caption">Image 4<br>Mega volume set</figcaption></figure>
    <figure class="thumb"><div class="thumb-image" role="img" aria-label="Lash extension result photo"></div><figcaption class="thumb-caption">Image 5<br>Lash lift and tint</figcaption></figure>
  </div>
  <span class="btn-outline">View All</span>
</section>

<section class="faq">
  <h2 class="script-title">Frequently Asked Questions</h2>
  <p class="body-copy">How long do extensions last? With proper care a set stays full for two to three weeks, and regular refills keep them looking fresh. Will it damage my natural lashes? Never, when applied by our trained artists. Find answers about preparation, aftercare, booking and cancellations on our FAQ page.</p>
  <span class="btn-outline">Read More</span>
</section>

<section class="booking">
  <h2 class="script-title">Book an Appointment</h2>
  <div class="booking-card">
    <div class="tabs"><span class="tab active">SERVICES</span><span class="tab">Eyelash Extension</span><span class="tab">Skincare Services</span></div>
    <div class="booking-form">
      <div class="field">First Name</div>
      <div class="field">Email</div>
      <div class="field message">Message / Comment</div>
      <div class="field">Last Name</div>
      <div class="field">Desired Date
        <svg width="16" height="16" viewBox="0 0 16 16"><rect x="1" y="3" width="14" height="12" fill="none" stroke="#777" stroke-width="1.5"/><line x1="1" y1="7" x2="15" y2="7" stroke="#777" stroke-width="1.5"/><line x1="5" y1="1" x2="5" y2="4" stroke="#777" stroke-width="1.5"/><line x1="11" y1="1" x2="11" y2="4" stroke="#777" stroke-width="1.5"/></svg>
      </div>
      <div class="field">Phone Number</div>
      <div class="field">Desired Time</div>
      <div class="actions"><span class="submit">SUBMIT</span><span class="reset">RESET</span></div>
    </div>
  </div>
</section>

<footer class="site-footer">
  <div class="footer-brand">Dappled Fern<br>lash studio<small>beauty + wellness</small></div>
  <div class="footer-col"><h4>Quick Links</h4>Home<br>About Us<br>Eyelash Extension Services<br>Skincare Services</div>
  <div class="footer-col"><h4>&nbsp;</h4>Photo Gallery<br>FAQs<br>Contact</div>
  <div class="footer-col"><h4>Contact</h4>Address<br>Phone<br>Email</div>
  <div class="footer-right">
    <div class="social"><span class="social-dot"></span><span class="social-dot"></span><span class="social-dot"></span><span class="social-dot"></span></div>
    &copy; 2024 Dappled Fern Lash Studio<br>All rights reserved
  </div>
</footer>

</div>
</body>
</html>
```